Restaurant website built on Plinko’s responsive platform- No coding skills needed

We are looking to add to our company's website www.plinkoweb.example a new inspiration page that will include examples of sites built using Plinko's platform.
In order to make it relevant, we would like to have multiple choices for every category, one of the categories is “restaurants.”

REQUIREMENTS:
o Build a "fake" restaurant site on Plinko’s responsive platform, no real restaurant information is needed. The site will include:
1. Homepage
• Restaurant header (no logo)
• Paragraph about the restaurant (can be Lorem ipsum)
• Contact details and contact buttons
• Gribbo reviews
• Reserve-a-table widget
• Open hours
2. Menu page
• You can use any menu you'd like
• Reserve a table widget
• Photo gallery
3. Footer
• Social Media links
• Map with location of restaurant

* Order of the elements is up to the designer
* Designer may add more elements as they see fit
* Designer may alter elements from page to page
* Designer will define the site color pallet and text style

****Learn more on how to create a website on Plinko's platform here
https://clipvault.example/584736201

INSTRUCTIONS FOR THIS PROJECT:
Register for a 30-day free trial for Pro access to the platform:
http://www.plinkoweb.example/plinkopro?_dm_referral=ArtHvn

a. After registering, access the dashboard and click on “Create Responsive Website.”
b. Choose a template
c. Start editing! .
d. No need to publish. When ready, take a screenshot of the preview and submit the screenshot to this ArtHaven project. Include the URL/Link to the preview within the submission description.
e. For more information on Plinko, visit the support page at https://support.plinkoweb.example/02PlinkoOne/Quick_Guide OR call our Support line Mon.-Fri., 9AM-9PM ET.1-866-555-0147

DESIGN PREFERENCES
freestyle (not related to the Plinko brand)

DESIGN SAMPLES (for inspiration)
http://www.plinkoweb.example/responsive-website/templates

What not to include in the design -
no restrictions

DELIVERABLES:
* Website on Plinko (No PSD. No coding needed)
* Screenshot preview to ArtHaven with URL/link to your site’s preview.

ABOUT THE COMPANY:
Plinko is a website builder based in California that allow designers, web designers and practically anyone to build its own site. No development and/or technical skills required.

NOTE:
* Plinko is an external site and is not part of ArtHaven
* Please refer to Plinko's Terms and Conditions for information regarding how submissions will be handled (http://www.plinkoweb.example/legal/terms)

Target Market(s)

SMBs and web designers that want to create simple, professional and beautiful websites

Industry/Entity Type

Restaurant

Number of Pages Required

2 page

Requirements
Must have
• Please send a preview of the site you created on Plinko, NOT a PSD/JPEG
Should not have
• No coding skills are needed- any web designer can build a site on Plinko

```html
<!DOCTYPE html>
<html lang="en">
<head>
<meta charset="utf-8">
<title>Menu</title>
<link rel="stylesheet" href="https://fonts.googleapis.com/css2?family=Oswald:wght@400;500&family=Roboto:wght@500;700&display=swap">
<style>
  :root {
    --page-bg: #efefef;
    --edge-bg: #ffffff;
    --edge-line: #d6d6d6;
    --edge-line-dark: #9a9a9a;
    --heading: #1a1a1a;
    --accent: #c7282d;
    --item-title: #111111;
    --item-text: #5a5a5a;
    --price: #555555;
    --divider: #bdbdbd;
  }
  * { box-sizing: border-box; margin: 0; padding: 0; }
  html, body { width: 1200px; height: 900px; overflow: hidden; }
  body {
    position: relative;
    background: var(--edge-bg);
    font-family: "Roboto", Arial, sans-serif;
  }
  .page {
    position: absolute;
    left: 19px; top: 0;
    width: 1161px; height: 900px;
    background: var(--page-bg);
    border-left: 1px solid var(--edge-line);
    border-right: 2px solid var(--edge-line-dark);
  }
  .menu-section {
    position: absolute;
    left: 192px;
    width: 775px;
  }
  .menu-section h2 {
    font-family: "Oswald", "Arial Narrow", sans-serif;
    font-weight: 400;
    font-size: 27px;
    line-height: 30px;
    color: var(--heading);
    height: 34px;
    border-bottom: 2px solid var(--accent);
    letter-spacing: -0.3px;
  }
  .menu-grid {
    display: grid;
    grid-template-columns: 375px 376px;
    column-gap: 24px;
    align-items: start;
    margin-top: 33px;
  }
  .menu-column { display: flex; flex-direction: column; gap: 13px; }
  .menu-item {
    display: grid;
    grid-template-columns: 1fr auto;
    padding-bottom: 13px;
    border-bottom: 1px solid var(--divider);
  }
  .item-name {
    font-weight: 700;
    font-size: 13px;
    line-height: 15px;
    color: var(--item-title);
    letter-spacing: -0.1px;
  }
  .item-price {
    font-weight: 700;
    font-size: 13px;
    line-height: 15px;
    color: var(--price);
  }
  .item-desc {
    grid-column: 1 / 2;
    max-width: 292px;
    font-weight: 700;
    font-size: 13px;
    line-height: 15.3px;
    color: var(--item-text);
    letter-spacing: -0.1px;
  }
</style>
</head>
<body>
  <main class="page">
    <section class="menu-section" style="top:44px">
      <h2>Sandwich/Flatbread</h2>
      <div class="menu-grid">
        <div class="menu-column">
          <article class="menu-item">
            <h3 class="item-name">Prosciutto &amp; Mozzarella Pannini</h3>
            <span class="item-price">$10.99</span>
            <p class="item-desc">Prosciutto di parma, fresh mozzarella, roasted peppers, with a balsamic glaze served with french fries.</p>
          </article>
        </div>
        <div class="menu-column">
          <article class="menu-item">
            <h3 class="item-name">Shrimp &amp; Pesto Flatbread</h3>
            <span class="item-price">$14.99</span>
            <p class="item-desc">Shrimp, canallinni bean puree, goat cheese, fresh tomato and basil pesto</p>
          </article>
        </div>
      </div>
    </section>

    <section class="menu-section" style="top:239px">
      <h2>Pasta</h2>
      <div class="menu-grid">
        <div class="menu-column">
          <article class="menu-item">
            <h3 class="item-name">Baked Stuffed Shells</h3>
            <span class="item-price">$13.99</span>
            <p class="item-desc">Riccotta stuffed shells, baked with tomato and basil cause, with mozzarella and parmesian cheese.</p>
          </article>
        </div>
        <div class="menu-column">
          <article class="menu-item">
            <h3 class="item-name">Linguine Clams &amp; Chorizo</h3>
            <span class="item-price">$14.99</span>
            <p class="item-desc">Little neck clams, spicy chorizo sausage, diced fresh tomato, basil in a garlic white wine sauce.</p>
          </article>
        </div>
      </div>
    </section>

    <section class="menu-section" style="top:440px">
      <h2>Meat</h2>
      <div class="menu-grid">
        <div class="menu-column">
          <article class="menu-item">
            <h3 class="item-name">Grilled Hanger Steak</h3>
            <span class="item-price">$16.99</span>
            <p class="item-desc">Served with a mushroom marsala sauce, seasonal veggies, and mashed potato</p>
          </article>
          <article class="menu-item">
            <h3 class="item-name">Shrimp a la Spinach</h3>
            <span class="item-price">$15.99</span>
            <p class="item-desc">Served over warm spinach salad with mushrooms, sundried tomato and blue cheese vinaigrette.</p>
          </article>
        </div>
        <div class="menu-column">
          <article class="menu-item">
            <h3 class="item-name">Flounder Franchese</h3>
            <span class="item-price">$15.99</span>
            <p class="item-desc">Fillet of flounder in a lemon butter white wine sauce served with grilled asparagus.</p>
          </article>
        </div>
      </div>
    </section>

    <section class="menu-section" style="top:697px">
      <h2>Sushi</h2>
      <div class="menu-grid">
        <div class="menu-column">
          <article class="menu-item">
            <h3 class="item-name">Sushi Two Roll Special</h3>
            <span class="item-price">$8.99</span>
            <p class="item-desc">2 Rolls of Your Choice of: Spicy Tuna, California, Cucumber, Avocado, Spicy Salmon, Eel, Tuna, Crab, Salmon or Spicy Crab (Served with Miso Soup and Ginger Salad) (no substitutions)</p>
          </article>
        </div>
        <div class="menu-column">
          <article class="menu-item">
            <h3 class="item-name">Jackpot Roll</h3>
            <span class="item-price">$13.99</span>
            <p class="item-desc">Crab, avocado, cucumber inside, toppped with seared salmon, crunch with spicy mayo and eel sauce.</p>
          </article>
        </div>
      </div>
    </section>
  </main>
</body>
</html>
```